stationary for home builder
Birchwood Custom Homes, Inc.
Project: stationary for home builder
stationary for home builder - Real Estate
Creative Brief
Professional
Dale Morrow
President
4200 Tern Avenue, suite 310 Alder Bay, CA 95555
bchdalemorrow@mailvista.test

```html
<!DOCTYPE html>
<html lang="en">
<head>
<meta charset="utf-8">
<title>Birchwood Custom Homes – Business Cards</title>
<link rel="stylesheet" href="https://fonts.googleapis.com/css2?family=Cinzel:wght@400;600&family=Cormorant+Garamond:wght@500;600&display=swap">
<style>
  :root {
    --bg: #e4e4e6;
    --card: #ffffff;
    --red: #c0272d;
    --red-dark: #8f1a1f;
    --grey: #8a8c90;
    --grey-light: #c9cacc;
    --text: #5b5d61;
  }
  * { box-sizing: border-box; margin: 0; padding: 0; }
  html, body { width: 1200px; height: 984px; overflow: hidden; }
  body {
    background: var(--bg);
    font-family: "Cormorant Garamond", Georgia, serif;
    color: var(--text);
    position: relative;
  }
  .card {
    position: absolute;
    left: 240px;
    width: 720px;
    height: 411px;
    background: var(--card);
    border-radius: 28px;
    overflow: hidden;
    box-shadow: 0 14px 30px rgba(0,0,0,.18);
  }
  .card--back { top: 54px; }
  .card--front { top: 519px; }

  .brand-mark { display: block; background: var(--red); flex: none; }
  .card--back .brand-mark {
    position: absolute; left: 328px; top: 110px;
    width: 64px; height: 64px;
  }
  .card--back .brand-name {
    position: absolute; left: 0; right: 0; top: 196px;
    text-align: center;
    font-family: "Cinzel", Georgia, serif;
    font-weight: 600; font-size: 22px; letter-spacing: 2px;
    color: var(--red);
  }
  .web-address {
    position: absolute; left: 0; right: 0; top: 262px;
    text-align: center;
    font-family: "Cinzel", Georgia, serif;
    font-size: 18px; letter-spacing: 1.5px;
    color: var(--red);
  }

  .brand-lockup {
    position: absolute; left: 0; right: 0; top: 40px;
    display: flex; align-items: center; justify-content: center; gap: 14px;
    white-space: nowrap;
  }
  .card--front .brand-mark { width: 44px; height: 44px; }
  .card--front .brand-name {
    font-family: "Cinzel", Georgia, serif;
    font-weight: 600; font-size: 25px; letter-spacing: 1px;
    color: var(--red);
  }

  .swoosh { position: absolute; left: 0; bottom: 0; width: 720px; height: 230px; }

  .contact {
    position: absolute; top: 112px;
    font-size: 15px; line-height: 21px;
    white-space: nowrap;
  }
  .contact--person { right: 378px; text-align: right; }
  .person-name {
    font-family: "Cinzel", Georgia, serif;
    font-weight: 600; font-size: 17px; color: var(--red);
  }
  .person-title { font-family: "Cinzel", Georgia, serif; font-size: 12px; letter-spacing: 1px; margin-bottom: 2px; }
  .contact-divider {
    position: absolute; left: 356px; top: 114px; width: 1px; height: 88px; background: var(--grey-light);
  }
  .contact--lines { left: 372px; list-style: none; }
  .contact--lines li { display: flex; align-items: center; gap: 8px; }
  .icon { width: 15px; height: 15px; flex: none; }
</style>
</head>
<body>

<section class="card card--back" aria-label="Card back">
  <span class="brand-mark" aria-hidden="true"></span>
  <p class="brand-name">Birchwood Custom Homes, Inc.</p>
  <p class="web-address">www.birchwoodhomes.test</p>
</section>

<section class="card card--front" aria-label="Card front">
  <div class="brand-lockup">
    <span class="brand-mark" aria-hidden="true"></span>
    <span class="brand-name">Birchwood Custom Homes, Inc.</span>
  </div>

  <svg class="swoosh" viewBox="0 0 720 230" preserveAspectRatio="none" aria-hidden="true">
    <defs>
      <linearGradient id="greyBand" x1="0" y1="0" x2="1" y2="0">
        <stop offset="0" stop-color="#6f7175"/>
        <stop offset=".5" stop-color="#d7d8da"/>
        <stop offset="1" stop-color="#8a8c90"/>
      </linearGradient>
      <linearGradient id="redBand" x1="0" y1="0" x2="1" y2="0">
        <stop offset="0" stop-color="#8f1a1f"/>
        <stop offset=".45" stop-color="#d63a3f"/>
        <stop offset="1" stop-color="#a31f25"/>
      </linearGradient>
    </defs>
    <path d="M0 72 C160 52 300 160 720 156 L720 230 L0 230 Z" fill="url(#greyBand)"/>
    <path d="M0 92 C170 78 300 178 720 174 L720 230 L0 230 Z" fill="#ffffff"/>
    <path d="M0 108 C180 98 320 196 720 190 L720 230 L0 230 Z" fill="url(#redBand)"/>
  </svg>

  <div class="contact contact--person">
    <p class="person-name">Dale Morrow</p>
    <p class="person-title">President</p>
    <p>4200 Tern Avenue, suite 310</p>
    <p>Alder Bay, CA 95555</p>
  </div>

  <span class="contact-divider" aria-hidden="true"></span>

  <ul class="contact contact--lines">
    <li>
      <svg class="icon" viewBox="0 0 16 16" aria-hidden="true"><circle cx="8" cy="8" r="8" fill="var(--red)"/><path d="M5 4.5c.6-.4 1.1-.2 1.4.4l.5 1c.2.4 0 .8-.3 1l-.4.3c.4.9 1 1.5 1.9 1.9l.3-.4c.2-.3.6-.5 1-.3l1 .5c.6.3.8.8.4 1.4-.6.9-1.7 1.1-2.7.5C6.3 10 6 9.7 5.2 8 4.5 6.6 4.3 5.2 5 4.5z" fill="#fff"/></svg>
      <span>555.201.4410</span>
    </li>
    <li>
      <svg class="icon" viewBox="0 0 16 16" aria-hidden="true"><circle cx="8" cy="8" r="8" fill="var(--red)"/><rect x="5.5" y="3.5" width="5" height="9" rx="1" fill="#fff"/></svg>
      <span>555.201.7732</span>
    </li>
    <li>
      <svg class="icon" viewBox="0 0 16 16" aria-hidden="true"><circle cx="8" cy="8" r="8" fill="var(--red)"/><rect x="4" y="5" width="8" height="6" fill="#fff"/><path d="M4 5l4 3.2L12 5" stroke="var(--red)" fill="none"/></svg>
      <span>bchdalemorrow@mailvista.test</span>
    </li>
    <li>
      <svg class="icon" viewBox="0 0 16 16" aria-hidden="true"><circle cx="8" cy="8" r="8" fill="var(--red)"/><circle cx="8" cy="8" r="4" fill="none" stroke="#fff"/><path d="M4 8h8M8 4v8" stroke="#fff"/></svg>
      <span>www.birchwoodhomes.test</span>
    </li>
  </ul>
</section>

</body>
</html>
```